Gardener needs an exciting new flyer design.

I'm a passionate gardener that requires a custom flyer design for a owner operator gardening business. Design will be for a DL flyer. I'm based on the Sunshine coast in Queensland Australia. My target audience is the residential market on the Sunshine coast. Business name is Corliss Yards. My services are, lawn mowing, weeding, Eco Friendly fertilizing, green waste removal, Mulching, tree and shrub pruning, Full garden makeovers, hedging, pressure cleaning, privacy screening, Timber deck rejuvenation, Planting, Turf preparation and installation, and much more. Free no obligation quotes, reliable and friendly service, great rates. 12 years experience. Web www.corlissyards.com.au - Phone 0491827365 - Email tom@corlissyards.com.au I would like the design to portray a friendly and professional approach.

Target Market(s)

Residential

Industry/Entity Type

Gardener

Font styles to use
Serif

Colors
9ccb3b
abd037
3176b5

Requirements
Must have
• my services, my logo, my contact details,

```html
<!DOCTYPE html>
<html lang="en">
<head>
<meta charset="utf-8">
<title>Corliss Yards – DL Flyer</title>
<link rel="stylesheet" href="https://fonts.googleapis.com/css2?family=Montserrat:wght@600;700;800&family=Oswald:wght@400;500&display=swap">
<style>
  :root {
    --lime: #6cbf2a;
    --forest: #0a7f35;
    --promo-dark: #2b9a3a;
    --promo-light: #6cbf2a;
    --ink: #111111;
    --ink-soft: #333333;
    --plum: #5a1f5e;
    --footer: #2e2b2b;
    --backdrop: #e9e8e6;
    --paper: #ffffff;
  }
  * { box-sizing: border-box; margin: 0; padding: 0; }
  html, body {
    width: 1200px; height: 1151px; overflow: hidden;
    background: var(--backdrop);
  }
  .flyer {
    position: absolute; left: 343px; top: 31px;
    width: 626px; height: 1328px;
    background: var(--paper);
    transform: scale(0.82); transform-origin: 0 0;
    font-family: "Montserrat", sans-serif;
    overflow: hidden;
  }
  .hero-shapes { position: absolute; inset: 0; width: 626px; height: 1328px; }

  .brand { position: absolute; left: 0; right: 0; top: 40px; text-align: center; padding-left: 352px; width: 626px; }
  .brand-block { position: absolute; left: 370px; top: 40px; width: 240px; text-align: center; }
  .brand-dot { width: 46px; height: 46px; border-radius: 50%; background: var(--forest); margin: 0 auto 18px; }
  .brand-name { font-weight: 700; font-size: 27px; color: var(--forest); letter-spacing: 0.3px; }
  .brand-url { margin-top: 14px; font-weight: 600; font-size: 14px; color: var(--plum); letter-spacing: 0.3px; }

  .headline {
    position: absolute; left: 17px; top: 525px;
    color: #fff; font-weight: 800; font-size: 28px; line-height: 45px;
    letter-spacing: 0.2px;
  }
  .services-title {
    position: absolute; right: 60px; top: 718px; text-align: right;
    color: var(--ink); font-weight: 800; font-size: 40px; line-height: 43px;
  }
  .services-box {
    position: absolute; left: 22px; top: 817px; width: 578px; height: 210px;
    border: 2px dashed #8fd07a;
  }
  .service-list {
    position: absolute; list-style: none;
    font-family: "Oswald", sans-serif; font-weight: 500; font-size: 20px;
    color: var(--ink); letter-spacing: 1px; line-height: 34px;
  }
  .service-list.left { left: 22px; top: 22px; }
  .service-list.right { left: 330px; top: 25px; }
  .service-list li::before { content: "- "; }
  .more {
    position: absolute; left: 0; right: 0; top: 165px; text-align: center;
    color: var(--promo-dark); font-weight: 700; font-size: 17px; letter-spacing: 2px;
  }

  .promo { position: absolute; left: 25px; top: 1038px; width: 576px; height: 102px; display: flex; color: #fff; }
  .promo-free { width: 223px; background: var(--promo-dark); text-align: center; padding-top: 18px; }
  .promo-rates { flex: 1; background: var(--promo-light); text-align: center; padding-top: 20px; }
  .promo-big { font-weight: 800; font-size: 46px; line-height: 46px; }
  .promo-rates .promo-big { font-size: 38px; line-height: 40px; }
  .promo-small { font-family: "Oswald", sans-serif; font-weight: 400; font-size: 17px; letter-spacing: 0.5px; }
  .promo-rates .promo-small { font-size: 26px; line-height: 30px; }

  .contact-head {
    position: absolute; left: 0; right: 0; top: 1170px; text-align: center;
    font-weight: 700; font-size: 16px; letter-spacing: 2.5px; color: var(--ink-soft);
  }
  .contact-line {
    position: absolute; top: 1206px; display: flex; align-items: center; gap: 6px;
    font-weight: 600; font-size: 15px; letter-spacing: 1.6px; color: var(--ink);
  }
  .contact-line.phone { left: 68px; }
  .contact-line.email { left: 253px; }
  .contact-line.phone span { font-weight: 700; }
  .footer {
    position: absolute; left: 0; right: 0; bottom: 0; height: 73px;
    background: var(--footer); color: #fff; text-align: center;
    font-weight: 600; font-size: 17px; letter-spacing: 2px; line-height: 73px;
  }
</style>
</head>
<body>
<main class="flyer">
  <svg class="hero-shapes" viewBox="0 0 626 1328" xmlns="http://www.w3.org/2000/svg">
    <defs>
      <linearGradient id="garden" x1="0" y1="0" x2="0" y2="1">
        <stop offset="0" stop-color="#2f6b2a"/>
        <stop offset="0.45" stop-color="#3f7f34"/>
        <stop offset="0.62" stop-color="#7a9a3e"/>
        <stop offset="0.75" stop-color="#3fa531"/>
        <stop offset="1" stop-color="#2f9a2a"/>
      </linearGradient>
    </defs>
    <g role="img" aria-label="Photo of a landscaped garden with trees, flowering beds and a green lawn">
      <polygon points="0,75 476,345 626,345 626,760 445,660 216,793 0,665" fill="url(#garden)"/>
    </g>
    <polygon class="band-top" points="0,0 28,0 560,300 476,345 0,75" fill="var(--lime)"/>
    <polygon class="corner-top" points="476,345 626,260 626,345" fill="var(--forest)"/>
    <polygon class="corner-bottom" points="0,665 151,750 216,793 0,750" fill="var(--forest)"/>
    <polygon class="band-bottom" points="626,475 626,555 216,793 151,750" fill="var(--lime)"/>
  </svg>

  <div class="brand-block">
    <div class="brand-dot"></div>
    <div class="brand-name">Corliss Yards</div>
    <div class="brand-url">corlissyards.com.au</div>
  </div>

  <h1 class="headline">A BEAUTIFUL<br>GARDEN DOESN'T<br>HAPPEN BY ITSELF</h1>

  <h2 class="services-title">OUR<br>SERVICES</h2>

  <section class="services-box">
    <ul class="service-list left">
      <li>Lawn Mowing</li>
      <li>Weeding</li>
      <li>Eco Friendly Fertilizing</li>
      <li>Green Waste Removal</li>
    </ul>
    <ul class="service-list right">
      <li>Full Garden Makeovers</li>
      <li>Hedging</li>
      <li>Pressure Cleaning</li>
      <li>Privacy Screening</li>
    </ul>
    <p class="more">...AND MUCH MORE</p>
  </section>

  <section class="promo">
    <div class="promo-free">
      <div class="promo-big">FREE!!</div>
      <div class="promo-small">NO OBLIGATION QUOTES</div>
    </div>
    <div class="promo-rates">
      <div class="promo-big">GREAT RATES!!</div>
      <div class="promo-small">RELIABLE &amp; FRIENDLY SERVICE</div>
    </div>
  </section>

  <p class="contact-head">FOR INQUIRIES, CONTACT US VIA:</p>
  <p class="contact-line phone">
    <svg width="20" height="20" viewBox="0 0 24 24" aria-hidden="true"><path fill="var(--promo-dark)" d="M6.6 10.8a15.1 15.1 0 0 0 6.6 6.6l2.2-2.2a1 1 0 0 1 1-.25 11.4 11.4 0 0 0 3.6.57 1 1 0 0 1 1 1V20a1 1 0 0 1-1 1A17 17 0 0 1 3 4a1 1 0 0 1 1-1h3.5a1 1 0 0 1 1 1c0 1.25.2 2.45.57 3.57a1 1 0 0 1-.25 1z"/></svg>
    <span>049 18 27 365</span>
  </p>
  <p class="contact-line email">
    <svg width="22" height="16" viewBox="0 0 22 16" aria-hidden="true"><rect x="1" y="1" width="20" height="14" fill="none" stroke="var(--promo-dark)" stroke-width="1.8"/><path d="M1 1l10 8 10-8M1 15l7-6M21 15l-7-6" fill="none" stroke="var(--promo-dark)" stroke-width="1.6"/></svg>
    tom@corlissyards.com.au
  </p>

  <footer class="footer">www.corlissyards.com.au</footer>
</main>
</body>
</html>
```